Medical Website - (plastic Surgery)

HERE is a "GUIDELINE" of What I need. Please, feel free to ask anything
https://www.filecrate.example/s/k8pwq2mzt/WEBPAGE%20MANUAL.pdf

I need you to design the page, you can do it in english, I'll translate it later. I need at least these pages

homepage
profile
contact me
Main procedures pages (like Breasts) - that has links to specific procedures like breast augmentation
blog

1) Business Name and business logo:
Evandro Tel6ra - Cirurgia Plástica
Logo:
https://www.filecrate.example/s/r3hvx9lqd/Logo%20Gold%204M-V0-FINAL.ai

Fonts
https://www.filecrate.example/sh/t5gnb2wce/AAQr7YuPlKoW3-EzZvHdSaRfN

Personal Pictures (notice that this are my personal pictures, it cannot be copied to use in any other place than my website)
https://www.filecrate.example/sh/w9dkf4hjx/AAPm2-LsQbVe8Nc1-TyGoWzUi

I Have a image stock files, so you can just use some samples and I'll replace them later.

Actual homepage
http://10.47.233.18/evandro-teixeira/index5.html

PSD files for some other pages
https://www.filecrate.example/sh/b2jqz7vnm/AAR-hX482TcLp37KeUwYsDf

2) Navigation Link Name:
www.evandroteixeira.example.br

3) Short Description
I’m a plastic surgeon. I work mostly doing aesthetic surgeries. The website will be use for me as my personal profissional website but keeping in mind that the final objective is to turn my name a “brand" linked to high quality services on plastic surgery.

4) Target Market /Audience:
85% are women, from 20 to 60 y.o.. Mostly of them with good economical condi6on, social class B, AB, A. (Almost all of them are social media connected, use smartphones, and most of them seek and think that plas6c surgery is something glamorous).

5) Webites I like

http://drvolpen.example

clean design, large icons illustrating procedures

http://drvolpen.example/Procedures
how this page organize procedures

http://www.refinedbodyartclinic.example.au
How procedures are organized by pics

http://www.lumenaestheticinstitute.example
Procedures pages
Contact page

Target Market(s)

85% are women, from 20 to 60 y.o.. Mostly of them with good economical condi6on, social class B, AB, A. (Almost all of them are social media connected, use smartphones, and most of them seek and think that plastic surgery is something glamorous).

Industry/Entity Type

Plastic

Font styles to use
Other font styles liked:
• Link already provided to the fonts

Requirements
Must have
• Use pics to illustrate procedures and fonts with enough size to older people read. As well, some people over 40 are not used to internet, so it must be user friendly, intuitive...

```html
<!DOCTYPE html>
<html lang="pt">
<head>
<meta charset="utf-8">
<title>Evandro Teixeira – Cirurgia Plástica</title>
<link href="https://fonts.googleapis.com/css2?family=Open+Sans:wght@300;400;600;700&display=swap" rel="stylesheet">
<style>
:root{
  --gold:#c9b07a;
  --gold-dark:#9c8452;
  --ink:#2e2e2e;
  --muted:#8a8a8a;
  --line:#e6e6e6;
  --soft:#f7f7f7;
  --footer:#2b231d;
  --footer-deep:#1f1a16;
  --footer-line:#4a4038;
  --white:#ffffff;
}
*{box-sizing:border-box;margin:0;padding:0}
html,body{width:1200px;height:2951px;overflow:hidden}
body{position:relative;font-family:"Open Sans",Arial,sans-serif;color:var(--ink);background:var(--white)}
.abs{position:absolute}
/* top bar */
.topbar{left:0;top:0;width:1200px;height:28px;border-bottom:1px solid var(--line);font-size:11px;color:var(--muted)}
.topbar .contact{left:44px;top:6px}
.topbar .account{right:58px;top:6px;word-spacing:12px}
/* header */
.header{left:0;top:28px;width:1200px;height:72px}
.brand{left:59px;top:18px;display:flex;align-items:center;gap:10px}
.brand-mark{width:30px;height:30px;background:var(--gold)}
.brand-name{font-size:25px;font-weight:700;color:var(--ink);letter-spacing:-.3px}
.nav{left:462px;top:26px;display:flex;gap:26px;font-size:13px;color:var(--ink)}
.nav .active{color:var(--gold);position:relative}
.nav .active::before{content:"";position:absolute;left:-4px;right:-4px;top:-27px;height:3px;background:var(--gold)}
.caret{font-size:9px;color:var(--muted)}
/* hero */
.hero{left:0;top:100px;width:1200px;height:408px;
  background:
    radial-gradient(ellipse 150px 200px at 790px 230px,#f4f1ee 0%,#e9e3de 45%,rgba(220,216,212,0) 100%),
    radial-gradient(ellipse 260px 260px at 810px 220px,rgba(236,234,232,.9) 0%,rgba(210,210,210,0) 100%),
    linear-gradient(90deg,#a4a4a4 0%,#bcbcbc 30%,#cfcfcf 55%,#c6c6c6 80%,#adadad 100%)}
.hero-title{left:115px;top:78px;width:400px;text-align:center;color:var(--white);font-weight:300;font-size:42px;line-height:62px}
.hero-rule{left:158px;top:218px;width:314px;height:1px;background:rgba(255,255,255,.8)}
.hero-sub{left:115px;top:224px;width:400px;text-align:center;color:var(--white);font-size:16px;font-weight:300}
.btn{display:flex;align-items:center;justify-content:center;background:var(--gold);color:var(--white);font-size:15px}
.hero .b1{left:190px;top:281px;width:130px;height:35px}
.hero .b2{left:328px;top:281px;width:134px;height:35px}
.hero-arrow{top:185px;width:26px;height:40px;background:rgba(255,255,255,.35);color:var(--white);font-size:20px;display:flex;align-items:center;justify-content:center}
/* specialties */
.h-section{width:1200px;text-align:center;font-weight:400;color:var(--ink)}
.spec-title{left:0;top:520px;font-size:40px}
.spec-intro{left:140px;top:578px;width:920px;text-align:center;font-size:15px;line-height:28px;color:var(--muted)}
.tile{top:669px;width:201px;height:201px}
.tile .label{position:absolute;left:0;bottom:8px;width:100px;height:32px;padding-left:32px;display:flex;align-items:center;background:rgba(201,176,122,.85);color:var(--white);font-size:15px;font-weight:600}
.t-face{background:radial-gradient(ellipse 90px 110px at 110px 95px,#f1d9c9 0%,#e2bfa8 55%,rgba(0,0,0,0) 100%),linear-gradient(90deg,#2a2624 0%,#6a5a50 25%,#d9b9a3 45%,#cfab94 85%,#3a3330 100%)}
.t-mama{background:radial-gradient(ellipse 110px 90px at 100px 120px,#e8b99c 0%,#d69f80 60%,rgba(0,0,0,0) 100%),linear-gradient(180deg,#f2f2f2 0%,#dcae92 30%,#cc9476 100%)}
.t-corpo{background:radial-gradient(ellipse 60px 120px at 100px 90px,#f0d3c1 0%,#e5c0a9 60%,rgba(0,0,0,0) 100%),linear-gradient(180deg,#e7eef2 0%,#eed6c6 40%,#f5f2f0 75%,#e3e8ec 100%)}
.t-homens{background:radial-gradient(ellipse 80px 100px at 100px 95px,#e0b79b 0%,#c99576 60%,rgba(0,0,0,0) 100%),linear-gradient(180deg,#5a4030 0%,#c8997c 35%,#d8ac90 100%)}
.t-estetica{background:radial-gradient(ellipse 70px 100px at 80px 100px,#ead2c3 0%,#d9b8a5 60%,rgba(0,0,0,0) 100%),linear-gradient(90deg,#c7c9cb 0%,#d6cfca 40%,#c9a995 75%,#d1d2d4 100%)}
/* surgery band */
.surgery{left:0;top:922px;width:1200px;height:282px;
  background:
    radial-gradient(ellipse 200px 120px at 620px 170px,#c9d4d3 0%,rgba(175,190,188,0) 100%),
    radial-gradient(ellipse 300px 200px at 120px 200px,#b9c4c0 0%,rgba(160,175,172,0) 100%),
    linear-gradient(90deg,#8ea3a0 0%,#a7b8b4 45%,#9fb1ad 70%,#b2c0bd 100%)}
/* doctor */
.doctor{left:0;top:1204px;width:1200px;height:440px;background:var(--soft)}
.doctor-photo{left:138px;top:16px;width:206px;height:377px;
  background:
    radial-gradient(ellipse 40px 50px at 103px 50px,#d7ab8e 0%,#c89678 60%,rgba(0,0,0,0) 100%),
    radial-gradient(ellipse 100px 150px at 103px 230px,#ffffff 0%,#f1f1f1 60%,rgba(0,0,0,0) 100%),
    linear-gradient(180deg,#fafafa,#eeeeee)}
.doctor-name{left:468px;top:68px;font-size:17px;font-weight:700}
.doctor-text{left:468px;top:122px;width:585px;font-size:16.5px;line-height:18px;color:#333}
.doctor-text p+p{margin-top:14px}
.doctor .more{left:826px;top:350px;width:197px;height:43px;font-size:14px;font-weight:600}
/* cta */
.cta{left:0;top:1648px;width:1190px;height:130px;background:var(--gold);color:var(--white)}
.cta-title{left:84px;top:24px;font-size:22px}
.cta-text{left:46px;top:68px;width:720px;font-size:15.5px;line-height:20px}
.cta-btn{left:877px;top:50px;width:199px;height:43px;background:var(--white);color:var(--gold);font-size:14px;font-weight:600;display:flex;align-items:center;justify-content:center}
/* news */
.news-title{left:0;top:1820px;font-size:44px;font-weight:300}
.news-rule{left:540px;top:1873px;width:90px;height:3px;background:var(--gold)}
.arrow{top:1972px;font-size:40px;font-weight:300;color:var(--gold)}
.card{top:1928px;width:265px}
.card .img{height:151px}
.n-diet{background:radial-gradient(ellipse 40px 30px at 150px 105px,#e28a3a 0%,rgba(226,138,58,0) 100%),radial-gradient(ellipse 70px 80px at 130px 55px,#d9a98a 0%,rgba(0,0,0,0) 100%),linear-gradient(180deg,#f1f1f1 0%,#e6e0dc 50%,#2c2a2a 78%,#f1f1f1 100%)}
.n-face{background:radial-gradient(ellipse 60px 75px at 110px 75px,#f2d6c6 0%,#e6c0aa 60%,rgba(0,0,0,0) 100%),linear-gradient(90deg,#f4f4f4,#eee6e1 60%,#f6f6f6)}
.n-doc{background:radial-gradient(ellipse 55px 75px at 120px 95px,#ffffff 0%,rgba(255,255,255,0) 100%),radial-gradient(ellipse 18px 22px at 120px 22px,#c79577 0%,rgba(0,0,0,0) 100%),linear-gradient(180deg,#fbfbfb,#f2f2f2)}
.card h3{margin-top:30px;font-size:17px;font-weight:700;color:var(--gold)}
.card p{margin-top:46px;font-size:12.5px;line-height:20px;color:var(--muted)}
.card .btn{margin-top:12px;width:130px;height:31px;font-size:12.5px}
/* newsletter */
.newsletter{left:0;top:2392px;width:1200px;height:100px;background:var(--gold)}
.newsletter-text{left:168px;top:40px;color:var(--white);font-size:15px;font-weight:600}
.newsletter-input{left:651px;top:33px;width:252px;height:38px;background:var(--white);color:#aaa;font-size:14px;padding:10px 20px}
.newsletter-btn{left:903px;top:33px;width:118px;height:38px;background:var(--gold-dark);color:var(--white);font-size:14px;display:flex;align-items:center;justify-content:center}
/* footer */
.footer{left:0;top:2492px;width:1200px;height:394px;background:var(--footer);color:#d9d2c8}
.fcol h4{font-size:20px;font-weight:400;color:var(--white)}
.fcol h4 b{font-weight:700}
.fcol ul{list-style:none;margin-top:22px;width:235px}
.fcol li{height:39px;border-bottom:1px solid var(--footer-line);font-size:12px;padding-top:10px;text-transform:uppercase}
.fcol li.hl{color:var(--gold)}
.field{position:absolute;left:663px;width:216px;height:35px;background:var(--white);color:#999;font-size:11px;padding:10px 12px}
.field::after{content:"";position:absolute;right:0;top:0;width:40px;height:35px;background:#e5e5e5}
.field.msg{height:107px}
.field.msg::after{display:none}
.send{left:749px;top:2834px;width:130px;height:32px;font-size:12px}
.fpanel{left:907px;top:2492px;width:238px;height:394px;background:var(--footer-deep)}
.fmark{left:104px;top:16px;width:30px;height:30px;background:var(--gold)}
.fbrand{left:0;top:54px;width:238px;text-align:center;font-size:22px;font-weight:700;color:var(--white)}
.ftag{left:24px;top:144px;width:200px;font-size:25px;line-height:27px;color:var(--white);text-transform:uppercase;font-weight:400}
.socials{left:24px;top:326px;display:flex;gap:4px}
.socials span{width:22px;height:22px;border-radius:50%;background:#8d8478}
/* bottom */
.bottom{left:0;top:2886px;width:1200px;height:65px;background:#17130f;color:#bdb5aa;font-size:12px}
.bottom .copy{left:116px;top:24px}
.bottom .links{left:698px;top:24px}
</style>
</head>
<body>

<div class="abs topbar">
  <div class="abs contact">☏ Contacte-nos: (047) 9555-0142 &nbsp;&nbsp; ✉ Email : info@evandroteixeira.example.br</div>
  <div class="abs account">Acessar Registrar</div>
</div>

<header class="abs header">
  <div class="abs brand"><span class="brand-mark"></span><span class="brand-name">Evandro Teixeira</span></div>
  <nav class="abs nav">
    <span class="active">Home</span>
    <span>Equipe <span class="caret">⌄</span></span>
    <span>Face</span>
    <span><span class="caret">⌄</span> Mama <span class="caret">⌄</span></span>
    <span>Corpo</span>
    <span><span class="caret">⌄</span> Homens <span class="caret">⌄</span></span>
    <span>Estética <span class="caret">⌄</span></span>
    <span>Contactos &amp; Marcações <span class="caret">⌄</span></span>
  </nav>
</header>

<section class="abs hero" role="img" aria-label="Retrato de mulher com traços de proporção facial sobre fundo de azulejos cinzentos">
  <h1 class="abs hero-title">Descubra<br>o seu novo “eu”</h1>
  <div class="abs hero-rule"></div>
  <div class="abs hero-sub">Beleza, Simetria, Equilíbrio, Proporção</div>
  <div class="abs btn b1">Contacte-nos</div>
  <div class="abs btn b2">Saiba mais</div>
  <div class="abs hero-arrow" style="left:14px">‹</div>
  <div class="abs hero-arrow" style="left:1160px">›</div>
</section>

<h2 class="abs h-section spec-title">Especialidades</h2>
<p class="abs spec-intro">Lorem ipsum dolor sit amet, consectetur adipiscing elit. Nam scelerisque faucibus risus non iaculis. Fusce a augue ante, pellentesque pretium erat. Fusce in turpis in velit tempor pretium. Integer a leo libero.</p>

<div class="abs tile t-face" style="left:47px" role="img" aria-label="Rosto feminino com marcações cirúrgicas"><span class="label">Face</span></div>
<div class="abs tile t-mama" style="left:273px" role="img" aria-label="Tronco feminino com marcações nos seios"><span class="label">Mama</span></div>
<div class="abs tile t-corpo" style="left:499px" role="img" aria-label="Abdómen feminino com marcações"><span class="label">Corpo</span></div>
<div class="abs tile t-homens" style="left:725px" role="img" aria-label="Retrato masculino"><span class="label">Homens</span></div>
<div class="abs tile t-estetica" style="left:951px" role="img" aria-label="Pele com tratamento estético"><span class="label">Estética</span></div>

<div class="abs surgery" role="img" aria-label="Equipa cirúrgica em sala de operações"></div>

<section class="abs doctor">
  <div class="abs doctor-photo" role="img" aria-label="Médico de bata branca com estetoscópio, braços cruzados"></div>
  <h3 class="abs doctor-name">Dr. Evandro Teixeira</h3>
  <div class="abs doctor-text">
    <p>Lorem ipsum dolor sit amet, consectetur adipiscing elit. Integer vehicula lacinia ipsum et accumsan. Aenean orci lorem, malesuada at dolor sed, feugiat mattis purus. Nam ac dui eu dui scelerisque bibendum in nec ipsum. Fusce viverra arcu ut dui vehicula, non facilisis ante rhoncus. Praesent sit amet felis gravida velit venenatis luctus eget et purus. Morbi enim neque, tincidunt iaculis neque sit amet, bibendum vestibulum ligula. Sed convallis ligula vel turpis sodales, sit amet iaculis dui pretium. Fusce tempus neque nec euismod viverra.</p>
    <p>Morbi enim neque, tincidunt iaculis neque sit amet, bibendum vestibulum ligula. Sed convallis ligula vel turpis sodales, sit amet iaculis dui pretium. Fusce tempus neque nec euismod viverra.</p>
  </div>
  <div class="abs btn more">LER MAIS</div>
</section>

<section class="abs cta">
  <div class="abs cta-title">Venha saber o que podemos fazer por si, sem custo.</div>
  <div class="abs cta-text">Lorem ipsum dolor sit amet, consectetur adipiscing elit. Praesent convallis, nunc et tristique lobortis, libero nisl ullamcorper libero, non tincidunt neque leo sit amet lacus.</div>
  <div class="abs cta-btn">MARCAÇÕES</div>
</section>

<h2 class="abs h-section news-title">Notícias e Artigos</h2>
<div class="abs news-rule"></div>
<div class="abs arrow" style="left:72px">&lt;</div>
<div class="abs arrow" style="left:1090px">&gt;</div>

<article class="abs card" style="left:138px">
  <div class="img n-diet" role="img" aria-label="Cintura feminina com fita métrica e fruta"></div>
  <h3>LOREM IPSUM</h3>
  <p>Sed a velit vitae nunc porta iaculis. Aliquam tempus rutrum diam, non tincidunt odio pharetra vitae. Nulla facilisi. Duis sed laoreet dui. Duis a risus nec erat tincidunt feugiat. Cras dui velit, luctus vitae volutpat vitae.</p>
  <div class="btn">Read more</div>
</article>
<article class="abs card" style="left:464px">
  <div class="img n-face" role="img" aria-label="Mulher a receber tratamento estético facial"></div>
  <h3>LOREM IPSUM</h3>
  <p>Sed a velit vitae nunc porta iaculis. Aliquam tempus rutrum diam, non tincidunt odio pharetra vitae. Nulla facilisi. Duis sed laoreet dui. Duis a risus nec erat tincidunt feugiat. Cras dui velit, luctus vitae volutpat vitae.</p>
  <div class="btn">Read more</div>
</article>
<article class="abs card" style="left:791px">
  <div class="img n-doc" role="img" aria-label="Médico de bata branca a apresentar"></div>
  <h3>LOREM IPSUM</h3>
  <p>Sed a velit vitae nunc porta iaculis. Aliquam tempus rutrum diam, non tincidunt odio pharetra vitae. Nulla facilisi. Duis sed laoreet dui. Duis a risus nec erat tincidunt feugiat. Cras dui velit, luctus vitae volutpat vitae.</p>
  <div class="btn">Read more</div>
</article>

<section class="abs newsletter">
  <div class="abs newsletter-text">Subcreva a Newsletter para receber notícias e dicas sobre saúde.</div>
  <div class="abs newsletter-input">Add your email adress</div>
  <div class="abs newsletter-btn">Subscrever</div>
</section>

<footer class="abs footer">
  <div class="abs fcol" style="left:112px;top:36px">
    <h4>Lista de <b>Intervenções</b></h4>
    <ul><li>Face</li><li>Corpo</li><li>Mamas</li><li>Estética</li><li>Pele</li><li>Agendamento de consultas</li></ul>
  </div>
  <div class="abs fcol" style="left:376px;top:36px">
    <h4>Saiba <b>Mais</b></h4>
    <ul><li>Notícias &amp; Blog</li><li>Procedimentos cirúrgicos</li><li>Clínicas</li><li>Equipa</li><li class="hl">Perguntas frequentes</li><li>Contactos</li></ul>
  </div>
  <div class="abs fcol" style="left:643px;top:36px"><h4>Entre em <b>Contato</b></h4></div>
</footer>
<div class="field" style="top:2596px">Enter your name</div>
<div class="field" style="top:2637px">Enter your email</div>
<div class="field" style="top:2677px">Enter your subject</div>
<div class="field msg" style="top:2720px">Enter your message</div>
<div class="abs btn send">
  <svg width="12" height="12" viewBox="0 0 12 12" style="margin-right:6px"><path d="M0 6 12 0 8 12 6 7z" fill="#fff"/></svg>Send Message
</div>

<aside class="abs fpanel">
  <div class="abs fmark"></div>
  <div class="abs fbrand">Evandro Teixeira</div>
  <div class="abs ftag">A delicada arte de equilibrar a ciência com a natureza</div>
  <div class="abs socials"><span></span><span></span><span></span><span></span><span></span><span></span></div>
</aside>

<div class="abs bottom">
  <div class="abs copy"><b>Copyright 2014</b> - Evandro Teixeira. Todos os direitos reservados.</div>
  <div class="abs links">Blog | Media | Perguntas Frequentes | Contactos</div>
</div>

</body>
</html>
```